New italian pizza restaurant in Australia, looking for a clean and crisp new take away leaflet de...

We require a leaflet for a take away menu / introduction to the area for our new italian pizza restaurant. AS we are a brand new business we need to get the word out about opening and specials as well as a takeaway menu. I have attached logo and menu items along with a basic design concept to help speed up the process.

Target Market(s)

Widest age range possible, families

Colors

Designer to choose colors to be used in the design.

```html
<!DOCTYPE html>
<html lang="en">
<head>
<meta charset="utf-8">
<title>Marlowe Pizzeria – Takeaway Menu</title>
<link rel="stylesheet" href="https://fonts.googleapis.com/css2?family=Oswald:wght@500;600&family=Questrial&display=swap">
<style>
  :root {
    --page: #dcdcd8;
    --sheet: #000000;
    --ink: #ffffff;
    --green: #2f8a4f;
    --frame: #3a7a56;
    --red: #e3231c;
    --orange: #ff5a1f;
    --tomato: #c8261c;
    --crust: #d89a4c;
  }
  * { box-sizing: border-box; margin: 0; padding: 0; }
  html, body { width: 1200px; height: 800px; overflow: hidden; }
  body {
    background: var(--page);
    font-family: "Questrial", "Century Gothic", sans-serif;
    color: var(--ink);
    position: relative;
  }
  .sheet {
    position: absolute;
    top: 197px;
    width: 580px;
    height: 406px;
    background: var(--sheet);
    display: flex;
    overflow: hidden;
    box-shadow: 0 6px 18px rgba(0,0,0,.25);
  }
  .sheet--inside { left: 14px; }
  .sheet--outside { left: 606px; }
  .panel {
    position: relative;
    width: 193.33px;
    padding: 36px 12px 10px 14px;
  }
  .panel__title {
    position: relative;
    z-index: 1;
    font-family: "Oswald", "Arial Narrow", sans-serif;
    font-weight: 600;
    color: var(--green);
    font-size: 14px;
    letter-spacing: .2px;
    line-height: 1;
    margin-bottom: 8px;
    text-transform: uppercase;
  }
  .panel__title .price { font-size: 8px; color: var(--ink); font-family: "Questrial", sans-serif; }
  .menu-list { list-style: none; position: relative; z-index: 1; }
  .menu-item {
    font-size: 6.6px;
    line-height: 1.25;
    margin-bottom: 6.5px;
  }
  .menu-item .num { color: var(--red); }
  .compact .menu-item { margin-bottom: 1px; }
  .note { font-size: 6.6px; margin: -4px 0 6px; }
  .block { margin-bottom: 10px; }
  .photo { position: absolute; }
  .photo--round { border-radius: 50%; }
  .pizza-top { left: 58px; top: -38px; width: 110px; height: 70px; border-radius: 0 0 55px 55px; background: radial-gradient(circle, #d34a2a 0%, #b9562a 55%, var(--crust) 80%); }
  .bowtie { right: 4px; top: 4px; width: 44px; height: 38px; background: radial-gradient(circle, #f3d27c, #e6b84d 70%, transparent 72%); }
  .tomatoes { left: 82px; bottom: 0; width: 110px; height: 48px; background: radial-gradient(ellipse at 50% 80%, var(--tomato), #8c1b14 60%, transparent 72%); }
  .spaghetti-plate { right: 18px; bottom: -60px; width: 134px; height: 134px; background: radial-gradient(circle, #e8873a 0%, #f1b45c 45%, #ffffff 62%); }
  .salad-plate { right: 8px; top: -24px; width: 70px; height: 54px; border-radius: 0 0 35px 35px; background: radial-gradient(circle, #5d8f3a 0%, #c9473a 40%, #f2f2f2 66%); }
  .salad-bowl { right: 8px; bottom: 2px; width: 50px; height: 80px; background: linear-gradient(180deg, rgba(230,70,50,.0) 0%, #e0543a 30%, #7fb24a 65%, #dfe8e0 100%); border-radius: 26px; opacity: .9; }
  .cover {
    width: 193.34px;
    padding: 14px;
    background: var(--frame);
  }
  .cover__photo {
    position: relative;
    height: 100%;
    background: radial-gradient(circle at 50% 52%, #6a4a2a 0%, #3c2a1e 35%, #1f1f1f 70%, #151515 100%);
    padding: 22px 8px 12px;
    display: flex;
    flex-direction: column;
    align-items: center;
    justify-content: space-between;
  }
  .brand { display: flex; flex-direction: column; align-items: center; gap: 6px; }
  .brand__dot { width: 14px; height: 14px; border-radius: 50%; background: var(--green); }
  .brand__name {
    font-family: "Questrial", sans-serif;
    font-size: 13px;
    color: var(--ink);
    text-align: center;
    letter-spacing: .5px;
  }
  .contact { font-size: 7.5px; line-height: 1.35; text-align: center; align-self: stretch; }
  .contact__label { color: var(--orange); }
  .contact p { margin-bottom: 4px; }
</style>
</head>
<body>

<section class="sheet sheet--inside" aria-label="Menu inside: pizza and pasta">
  <div class="panel">
    <div class="photo pizza-top" role="img" aria-label="Photo of a sliced pizza from above"></div>
    <h2 class="panel__title">Pizza</h2>
    <ol class="menu-list">
      <li class="menu-item"><span class="num">1.</span> Capricciosa – tomato, cheese, ham, mushrooms, olives<br>Small $9 Large $15 Family $18</li>
      <li class="menu-item"><span class="num">2.</span> Napoli – tomato, cheese, olives, anchovies<br>Small $9 Large $15 Family $18</li>
      <li class="menu-item"><span class="num">3.</span> American – tomato, cheese, salami<br>Small $9 Large $15 Family $18</li>
      <li class="menu-item"><span class="num">4.</span> Vegetarian – tomato, cheese, mushroom, onions, capsicum, olives<br>Small $9 Large $15 Family $18</li>
      <li class="menu-item"><span class="num">5.</span> Seafood – tomato, cheese, prawns, clams, anchovies<br>Small $9.5 Large $15.5 Family $19</li>
      <li class="menu-item"><span class="num">6.</span> The Hot One – tomato, cheese, ham, salami, chilli<br>Small $9 Large $15 Family $18</li>
      <li class="menu-item"><span class="num">7.</span> Margherita – tomato, cheese, oregano<br>Small $8.5 Large $14.5 Family $17</li>
      <li class="menu-item"><span class="num">8.</span> The Lot – tomato, cheese, ham, salami, bacon, mushroom, onions, capsicum, pineapple, olives<br>Small $10 Large $16 Family $19</li>
      <li class="menu-item"><span class="num">9.</span> Mexican – tomato, cheese, salami, capsicum, chilli<br>Small $9 Large $15 Family $18</li>
    </ol>
    <div class="photo tomatoes" role="img" aria-label="Photo of cherry tomatoes on the vine"></div>
  </div>

  <div class="panel">
    <div class="photo bowtie" role="img" aria-label="Photo of bow-tie pasta pieces"></div>
    <h2 class="panel__title">Pizza</h2>
    <ol class="menu-list">
      <li class="menu-item"><span class="num">10.</span> Chicken – tomato, cheese, chicken, BBQ sauce<br>Small $9 Large $15 Family $18</li>
      <li class="menu-item"><span class="num">11.</span> Meat Lovers – tomato, cheese, ham, salami, bacon, BBQ sauce<br>Small $10 Large $16 Family $19</li>
      <li class="menu-item"><span class="num">12.</span> The House Pizza – tomato, cheese, ham, mushroom, capsicum<br>Small $9 Large $15 Family $18</li>
      <li class="menu-item"><span class="num">13.</span> Ceaser's Pizza – tomato, cheese, ham, mushroom, pineapple, prawns<br>Small $10 Large $16 Family $19</li>
      <li class="menu-item"><span class="num">14.</span> The Breakie Pizza – tomato, cheese, bacon, egg<br>Small $9 Large $15 Family $18</li>
      <li class="menu-item"><span class="num">15.</span> The Footy Special – tomato, cheese, ham, capsicum, onions, pineapple<br>Small $9 Large $15 Family $18</li>
      <li class="menu-item"><span class="num">16.</span> The Marlowe – tomato, cheese, ham, mushrooms, onions, olives<br>Small $9 Large $15 Family $18</li>
      <li class="menu-item"><span class="num">17.</span> The Harbour Special – tomato, cheese, ham, onions, bacon, egg<br>Small $10 Large $16 Family $19</li>
      <li class="menu-item"><span class="num">18.</span> Ham – tomato, cheese, ham<br>Small $8.5 Large $14.5 Family $17</li>
      <li class="menu-item"><span class="num">19.</span> Garlic – garlic, cheese, oregano<br>Small $8.5 Large $14.5 Family $17</li>
    </ol>
  </div>

  <div class="panel">
    <h2 class="panel__title">Pasta</h2>
    <p class="menu-item">Spaghetti, Penne, Gnocchi, Fettucine, Linguine</p>
    <ol class="menu-list">
      <li class="menu-item"><span class="num">1.</span> Bolognese – traditional meat sauce $14</li>
      <li class="menu-item"><span class="num">2.</span> Carbonara – bacon, egg and creamy parmesan sauce $14.5</li>
      <li class="menu-item"><span class="num">3.</span> Napolitana – basil and Napoli sauce $13.5</li>
      <li class="menu-item"><span class="num">4.</span> Amatriciana – bacon, capsicum, fresh chilli, Napoli sauce $14.5</li>
      <li class="menu-item"><span class="num">5.</span> Marinara – prawns, scallops, clams in Napoli sauce $16.5</li>
      <li class="menu-item"><span class="num">6.</span> Risotto Polo – chicken, mushroom, onion, cooked in a cream sauce $16.5</li>
      <li class="menu-item"><span class="num">7.</span> Lasagna – Homemade Lasagna $15</li>
      <li class="menu-item"><span class="num">8.</span> Pasta Your way- choose any three ingredients with cream or Napoli sauce $14.5</li>
    </ol>
    <div class="photo photo--round spaghetti-plate" role="img" aria-label="Photo of a plate of spaghetti with tomato sauce and feta"></div>
  </div>
</section>

<section class="sheet sheet--outside" aria-label="Menu outside: mains, extras and cover">
  <div class="panel">
    <div class="photo salad-plate" role="img" aria-label="Photo of a salmon salad plate"></div>
    <h2 class="panel__title">Main Meals</h2>
    <p class="note">(all mains served with chips or salad)</p>
    <ol class="menu-list">
      <li class="menu-item"><span class="num">1.</span> Scotch Fillet Steak 300g &nbsp; $25<br>grass fed, with your choice of Mushroom, Pepper or Garlic sauce</li>
      <li class="menu-item"><span class="num">2.</span> Calamari $19.5<br>Flash fried or crumbed squid with aioli</li>
      <li class="menu-item"><span class="num">3.</span> Chicken Parmigiana $19.5<br>Schnitzel topped with ham, Napoli sauce &amp; mozzarella</li>
      <li class="menu-item"><span class="num">4.</span> Veal Scallopini - with your choice of mushroom or creamy avocado sauce $19.5</li>
      <li class="menu-item"><span class="num">5.</span> Veal Parmigiana -schnitzel topped ham, Napoli sauce &amp; mozzarella $19.5</li>
    </ol>
    <h2 class="panel__title">Salads</h2>
    <ol class="menu-list">
      <li class="menu-item"><span class="num">1.</span> Greek Salad – cos lettuce, tomato, onion, cucumber, olives, feta cheese &amp; dressing $14.5</li>
      <li class="menu-item"><span class="num">2.</span> Grilled Chicken Salad – Seasoned chicken, mixed leaves, cherry tomato, Spanish onion, cucumber with garlic infused olive oil $15.5</li>
      <li class="menu-item"><span class="num">3.</span> Chicken Ceasar Salad – Chicken, cos lettuce, croutons, shaved parmesan, anchovies, egg, bacon served with ceaser dressing $15.5</li>
    </ol>
    <div class="photo salad-bowl" role="img" aria-label="Photo of salad ingredients falling into a glass bowl"></div>
  </div>

  <div class="panel">
    <div class="block">
      <h2 class="panel__title">Kids Menu <span class="price">$9.5</span></h2>
      <ol class="menu-list compact">
        <li class="menu-item"><span class="num">1.</span> Pasta Bolognese</li>
        <li class="menu-item"><span class="num">2.</span> Pasta Napoli</li>
        <li class="menu-item"><span class="num">3.</span> Chicken Nuggets &amp; Chips</li>
        <li class="menu-item"><span class="num">4.</span> Cheeseburger &amp; Chips</li>
      </ol>
    </div>
    <div class="block">
      <h2 class="panel__title">Sides</h2>
      <ul class="menu-list compact">
        <li class="menu-item">Garlic Bread $4.5</li>
        <li class="menu-item">Chips $7.5</li>
        <li class="menu-item">Garden Salad $5</li>
      </ul>
    </div>
    <div class="block">
      <h2 class="panel__title">Desserts</h2>
      <ul class="menu-list compact">
        <li class="menu-item">Gelati 500mls Varieties $6.5</li>
        <li class="menu-item">Baci $6</li>
        <li class="menu-item">Tartufo $6</li>
        <li class="menu-item">Chocolate Mousse $6</li>
      </ul>
    </div>
    <div class="block">
      <h2 class="panel__title">Drinks</h2>
      <ul class="menu-list compact">
        <li class="menu-item">Soft drinks 375ml - $2.5</li>
        <li class="menu-item">Soft drinks 1.25L - $4.5</li>
        <li class="menu-item">Water 600ml - $2.5</li>
      </ul>
    </div>
    <div class="block">
      <h2 class="panel__title">Combo Deals</h2>
      <ol class="menu-list">
        <li class="menu-item"><span class="num">1.</span> Any 2 Family pizzas, garlic bread and 1.25l soft drink - $41.00</li>
        <li class="menu-item"><span class="num">2.</span> 1 Large pizza, 1 pasta, garlic bread and 1.25l soft drink - $38.00</li>
        <li class="menu-item"><span class="num">3.</span> 2 Large pizzas, 1 garlic bread and 1.25l soft drink - $36.00</li>
      </ol>
    </div>
  </div>

  <div class="cover">
    <div class="cover__photo" role="img" aria-label="Photo of a vegetable pizza on a dark table with cherry tomatoes">
      <div class="brand">
        <span class="brand__dot"></span>
        <span class="brand__name">Marlowe Pizzeria</span>
      </div>
      <div class="contact">
        <p><span class="contact__label">Address:</span><br>12 Harbour St,<br>Westhaven 3050</p>
        <p><span class="contact__label">Tel:</span> 000 555 0192</p>
        <p><span class="contact__label">Website/ Online ordering:</span><br>www.marlowepizzeria.com</p>
      </div>
    </div>
  </div>
</section>

</body>
</html>
```